Sedona Themed Wedding Invitation & RSVP

*We have added our "Save the Date" for reference. We are not looking for an exact match, but we'd like the invitation and the "Save the Date" to coordinate. Our wedding colors are light pink, light green, cream, and gold. We have also added pictures of bouquets to give you an idea of the color palette and also examples of flowers and greenery to use in the invitation. What we like about the "Save the Date" is that it draws on the wedding colors and brings them in through the colors of the sunset.
*We have also added additional pictures the venue, the Le Verger Lodge, and several maps. We hope that you can use these to get a better feel for our venue and the theme of our wedding. It will be soft and romantic and at the very height of spring.
* We appreciated that many designers incorporated the Lodge at Le Vergre, we'd like to see more of that.
*Please note that we included some photos of Sedona for inspiration, please do not feel tied to these, do your own research and find what works best with your design.
*These maps are being included as references, but they are the work of other artists. Please make your own map from scratch and use these as references.
We would like a vertical quad-fold wedding invitation that has a perforated edge RSVP which can be sent as a postcard.
We have attached pictures of a similar style of invitation to serve as an example of the overall style we are looking for. We would like to see the end project be in a similar style of watercolor, but it would be Sedona themed throughout (rather than the forest theme presented in the attached example). We have also attached pictures of Sedona to serve as further inspiration. Below, we have provided an outline organized by panel (four panels on the front and four panels on the back) with descriptions of the more specific details:
-Front four panels:
-Panel 1: "Please join us for the wedding of Tobias and Colette"
-Panel 2: "Come out and celebrate. [INSERT TIME OF WEDDING HERE]
Saturday, May First 2021 at Le Verger de Rimoux"
-Panel 3: Custom map of Sedona. Include Le Verger de Rimoux on the
map (exemplar picture is of an idea for this is also included below)
- Panel 4: RSVP similar to one in the exemplar invitation. For RSVP date
deadline use April 1st, 2021. Address is 2287 W Marlow St Phoenix, AZ
85019
-Back four panels:
-Panel 1: Venue: Le Verger de Rimoux. 418 Fennick Ln, Sedona, AZ 86339.
Please arrive no earlier than XXX PM when valet services begin. Dinner
and dancing to follow the ceremony
-Panel 2: Hotels: Le Verger de Rimoux 418 Fennick Ln, Sedona, AZ 86339
(800) 612-3908; Bramwell Inn 917 N Tolliver Rd, Sedona, AZ 86339
(855) 238-6041.
"Hotel reservations can also be made through the links provided on our
website"
- Panel 3: "We have reserved a block of rooms for our guests. Please
mention the Pruett Halloway Wedding when you call to reserve."
"For additional details, please visit our wedding website and take a walk
down memory lane with us as we prepare to celebrate the rest of our
lives together: [INSERT WEDDING WEBSITE HERE AND
PASSWORD]"
- Panel 4: "Ceremony and celebration will be outdoors. Semi-formal attire
and flat shoes are recommended."
"Additionally, although we love your children, we want our wedding to
be your night off! Please know space is very limited; accordingly, we
encourage a weekend getaway for the grownups."
We'd like to have a succulent and rose at the bottom of the panel (an
exemplar picture is of an idea for this is also included below)
Updates
We have given extensive feedback to designers and would like to give them time to adjust their designs. Additionally, we have incorporated a lot more images into the brief that we hope will help!

```html
<!DOCTYPE html>
<html lang="en">
<head>
<meta charset="utf-8">
<title>Tobias &amp; Colette — Quad-fold Wedding Invitation</title>
<link href="https://fonts.googleapis.com/css2?family=Montserrat:wght@400&family=Oswald:wght@500&family=Pathway+Gothic+One&family=Kaushan+Script&family=Playball&family=Dancing+Script:wght@500&display=swap" rel="stylesheet">
<style>
:root{
  --ribbon:#d2382b;
  --red:#dc2b2b;
  --brown:#5a4520;
  --paper:#efe7d6;
  --paper-edge:#e9c9a0;
  --white:#ffffff;
  --cond:'Pathway Gothic One', sans-serif;
  --script:'Kaushan Script', cursive;
  --name:'Playball', cursive;
  --italic:'Dancing Script', cursive;
}
*{margin:0;padding:0;box-sizing:border-box}
html,body{width:855px;height:1200px;overflow:hidden;background:var(--white)}
.canvas{position:relative;width:855px;height:1200px;background:var(--white)}

.ribbon{position:absolute;top:47px;height:77px;background:var(--ribbon);color:var(--white);
  font-family:'Montserrat',sans-serif;font-size:50px;letter-spacing:2px;line-height:77px}
.ribbon--front{left:0;width:318px;padding-left:74px;clip-path:polygon(0 0,100% 0,94% 50%,100% 100%,0 100%)}
.ribbon--back{left:537px;width:318px;padding-left:97px;clip-path:polygon(0 0,100% 0,100% 100%,0 100%,6% 50%)}

.sheet{position:absolute;top:177px;width:322px;height:953px}
.sheet--front{left:71px}
.sheet--back{left:465px}

.panel{position:absolute;left:0;width:322px;overflow:hidden}
.paper{background:
  radial-gradient(ellipse 75% 70% at 50% 50%,var(--paper) 55%,#ecdcc0 85%,var(--paper-edge) 100%);}
.p1{top:0;height:241px}.p2{top:241px;height:236px}.p3{top:477px;height:236px}.p4{top:713px;height:240px}

.line{position:absolute;left:0;width:100%;text-align:center;white-space:nowrap}

/* front panel 1 */
.scene{position:absolute;inset:0;background:
  linear-gradient(180deg,#aab8c4 0%,#c4ccd2 22%,#c63a1f 40%,#b8361c 58%,#7a3a1e 70%,#3e5a2c 80%,#2b4a22 100%)}
.invite-top{font-family:var(--cond);color:var(--brown);font-size:11px;letter-spacing:3px;top:18px}
.invite-for{font-family:var(--italic);color:var(--brown);font-size:15px;top:30px}
.invite-wedding{font-family:'Oswald',sans-serif;color:var(--red);font-size:29px;letter-spacing:1px;top:46px}
.invite-of{position:absolute;left:139px;top:91px;width:46px;height:16px;background:#4a3a1a;color:var(--paper);
  font-family:var(--cond);font-size:11px;text-align:center;line-height:16px}
.couple{position:absolute;color:var(--white);font-family:var(--script);white-space:nowrap}
.couple--first{left:88px;top:122px;font-size:46px;transform:rotate(-8deg)}
.couple--and{left:78px;top:200px;font-size:20px;transform:rotate(-8deg)}
.couple--second{left:122px;top:170px;font-size:46px;transform:rotate(-8deg)}

/* front panel 2 */
.celebrate{font-family:var(--cond);color:var(--brown);font-size:20px;letter-spacing:1px;top:26px}
.month{font-family:var(--script);color:var(--brown);font-size:88px;top:40px;line-height:1.2}
.date-block{position:absolute;left:40px;top:173px;font-family:var(--cond);color:var(--brown)}
.date-block .big{font-size:24px;letter-spacing:1px;line-height:24px}
.date-block .sat{font-size:16px;line-height:18px;display:flex;align-items:center;gap:6px}
.date-block .bar{display:inline-block;width:2px;height:12px;background:var(--red)}
.date-block .time{font-size:6px;line-height:6px;width:38px}
.at-badge{position:absolute;left:152px;top:176px}
.venue-inline{position:absolute;left:197px;top:166px;font-family:var(--name);color:var(--brown);font-size:18px;line-height:20px}

/* map */
.map{position:absolute;inset:0;background:
  radial-gradient(ellipse at 40% 40%,#e8efd8 0%,#cfe3c4 45%,#a9d0a8 80%,#94c6a2 100%)}

/* rsvp */
.respond{position:absolute;left:22px;top:22px;width:150px;text-align:center;font-family:var(--cond);color:var(--brown);font-size:11px;letter-spacing:3px}
.deadline{position:absolute;left:26px;top:42px;display:flex;align-items:center;gap:6px;font-family:var(--cond);color:var(--brown)}
.deadline .small{font-size:20px;border-top:1px solid var(--brown);border-bottom:1px solid var(--brown);line-height:20px}
.deadline .huge{font-size:50px;font-family:'Oswald',sans-serif;line-height:52px}
.mline{position:absolute;left:26px;top:100px;width:145px;height:21px;border-bottom:1.5px solid var(--brown);
  font-family:var(--italic);color:var(--brown);font-size:20px;line-height:20px}
.mline2{position:absolute;left:26px;top:131px;width:145px;border-bottom:1.5px solid var(--brown)}
.choice{position:absolute;left:26px;display:flex;align-items:baseline;gap:4px;font-family:var(--italic);white-space:nowrap}
.choice .dot{width:9px;height:9px;border:1px solid var(--brown);border-radius:50%;align-self:center}
.choice .word{color:var(--red);font-size:13px}
.choice .note{color:var(--brown);font-size:7px}
.fav{position:absolute;left:26px;top:193px;width:145px;text-align:center;font-family:var(--italic);color:var(--red);font-size:10px}
.favline{position:absolute;left:26px;top:215px;width:145px;border-bottom:1.5px solid var(--brown)}
.initials{position:absolute;left:190px;top:42px;width:112px;text-align:center;font-family:var(--script);color:var(--brown);font-size:46px;line-height:52px}
.initials span{font-size:22px}
.address{position:absolute;left:180px;top:108px;width:132px;text-align:center;font-family:var(--cond);color:var(--brown);font-size:16px;line-height:18px}

/* back */
.headline{font-family:var(--script);color:var(--red);font-size:62px;line-height:1.1}
.place{font-family:var(--name);color:var(--brown);font-size:21px;line-height:24px}
.place--sm{font-size:19px}
.addr{font-family:var(--cond);color:var(--brown);font-size:15px;line-height:18px}
.addr--sm{font-size:9px;line-height:12px;word-spacing:2px}
.addr--sm em{font-style:normal;color:var(--red)}
.note{font-family:var(--cond);color:var(--brown);font-size:10px;line-height:13px;word-spacing:2px}
.caps{font-family:var(--cond);color:var(--brown);font-size:13px;line-height:16px;word-spacing:1px}
.mention{font-family:var(--name);color:var(--red);font-size:20px;line-height:24px}
.soft{font-family:var(--italic);color:var(--brown);font-size:12px;line-height:16.5px}
.website{font-family:var(--cond);color:var(--red);font-size:11.5px;line-height:14px;word-spacing:1px}
.plain{font-family:var(--cond);color:var(--brown);font-size:11.5px;line-height:15px}
.bouquet{position:absolute;left:100px;top:148px;width:121px;height:72px;border-radius:40px;
  background:radial-gradient(circle at 50% 45%,#9cc7a4 0%,#9cc7a4 22%,#e58a98 38%,#d9697c 60%,#3d5a32 85%,transparent 100%)}
</style>
</head>
<body>
<div class="canvas">
  <div class="ribbon ribbon--front">FRONT</div>
  <div class="ribbon ribbon--back">BACK</div>

  <section class="sheet sheet--front">
    <div class="panel p1">
      <div class="scene" role="img" aria-label="Photograph of Sedona's red rock buttes above green trees under a pale sky"></div>
      <div class="line invite-top">— PLEASE JOIN US —</div>
      <div class="line invite-for">for the</div>
      <div class="line invite-wedding">·WEDDING·</div>
      <div class="invite-of">OF</div>
      <div class="couple couple--first">Tobias</div>
      <div class="couple couple--second">Colette</div>
      <div class="couple couple--and">and</div>
    </div>

    <div class="panel paper p2">
      <div class="line celebrate">• COME OUT AND CELEBRATE •</div>
      <div class="line month">May</div>
      <div class="date-block">
        <div class="big">FIRST&nbsp; 2021</div>
        <div class="sat">SATURDAY <span class="bar"></span><span class="time">[INSERT TIME OF WEDDING HERE]</span></div>
      </div>
      <svg class="at-badge" width="36" height="22" viewBox="0 0 36 22">
        <polygon points="6,1 30,1 35,11 30,21 6,21 1,11" fill="none" stroke="#dc2b2b" stroke-width="1"/>
        <text x="18" y="15" text-anchor="middle" font-family="Dancing Script, cursive" font-size="12" fill="#5a4520">at</text>
      </svg>
      <div class="venue-inline">Le Verger<br>de Rimoux</div>
    </div>

    <div class="panel p3">
      <div class="map" role="img" aria-label="Watercolor map of Sedona marking Le Verger de Rimoux, roads, creek and nearby rock landmarks"></div>
    </div>

    <div class="panel paper p4">
      <div class="respond">— PLEASE RESPOND BY —</div>
      <div class="deadline"><span class="small">April</span><span class="huge">1st</span><span class="small">2021</span></div>
      <div class="mline">M</div>
      <div class="mline2"></div>
      <div class="choice" style="top:149px"><span class="dot"></span><span class="word">Yes!</span><span class="note">I'm ready to attack the dance floor</span></div>
      <div class="choice" style="top:166px"><span class="dot"></span><span class="word">No!</span><span class="note">I will forever regret this decision</span></div>
      <div class="fav">Favorite Song...</div>
      <div class="favline"></div>
      <div class="initials">T<span>&amp;</span>C</div>
      <div class="address">2287<br>W Marlow St Phoenix,<br>AZ 85019</div>
    </div>
  </section>

  <section class="sheet sheet--back">
    <div class="panel paper p1">
      <div class="line headline" style="top:28px">Venue</div>
      <div class="line place" style="top:114px">Le Verger de Rimoux</div>
      <div class="line addr" style="top:146px">418 Fennick Ln, Sedona, AZ 86339</div>
      <div class="line note" style="top:182px">Please arrive no earlier than XXX PM when valet services begin.</div>
      <div class="line note" style="top:196px">Dinner and dancing to follow the ceremony.</div>
    </div>

    <div class="panel paper p2">
      <div class="line headline" style="top:24px">Hotel</div>
      <div class="line place place--sm" style="top:110px">Le Verger de Rimoux</div>
      <div class="line addr addr--sm" style="top:136px">418 Fennick Ln, Sedona, AZ 86339 &nbsp;<em>(800) 612-3908</em></div>
      <div class="line place place--sm" style="top:155px">Bramwell Inn</div>
      <div class="line addr addr--sm" style="top:177px">917 N Tolliver Rd, Sedona, AZ 86339 &nbsp;<em>(855) 238-6041</em></div>
      <div class="line addr addr--sm" style="top:200px">“Hotel reservations can also be made through the links provided on our website”</div>
    </div>

    <div class="panel paper p3">
      <div class="line caps" style="top:34px">WE HAVE RESERVED A BLOCK OF ROOMS FOR OUR GUESTS</div>
      <div class="line mention" style="top:62px">• Please Mention •</div>
      <div class="line caps" style="top:90px">THE PRUETT HALLOWAY WEDDING WHEN YOU CALL TO RESERVE.</div>
      <div class="line soft" style="top:121px">For additional details, please visit our wedding website</div>
      <div class="line soft" style="top:138px">and take a walk down memory lane with us</div>
      <div class="line soft" style="top:154px">as we prepare to celebrate the rest of our lives together.</div>
      <div class="line website" style="top:187px">[INSERT WEDDING WEBSITE AND PASSWORD HERE]</div>
    </div>

    <div class="panel paper p4">
      <div class="line plain" style="top:24px">Ceremony and celebration will be outdoors.</div>
      <div class="line plain" style="top:39px">Semi formal attire and flat shoes are recommended.</div>
      <div class="line soft" style="top:65px">Additionally, although we love your children,</div>
      <div class="line soft" style="top:81px">we want our wedding to be your night off!</div>
      <div class="line soft" style="top:97px">Please know space is very limited; accordingly,</div>
      <div class="line soft" style="top:114px">we encourage a weekend getaway for the grownups.</div>
      <div class="bouquet" role="img" aria-label="Watercolor posy of pink roses around a pale green succulent with dark leaves"></div>
    </div>
  </section>
</div>
</body>
</html>
```